Los Fogones Ember Poultry MENU!

We are looking for a simple, rustic and modern menu that highlights our passion for healthy and tasty chickens!
We want to highlight our menu but yet keep it very simple.

Attached is info on our logo and our menu information

Target Market(s)

We want to attract all customers but primarily we want to focus on the following 3 markets: Healthy concerned, Food fanatics and Family based.

Industry/Entity Type

Fast Food Restaurant

Requirements
Must have
• We must have our logo on the flyer,
• rustic yet modern
• you must use our colors on the flyer and
• KEEP IT SIMPLE
• Here is our Menu below
• Attached is our final menu we are going to advertise:
• Chicken:
• 1/4 Chicken Dark $6.99
• 1/4 Chicken White $7.99
• 1/2 Chicken white + dark $9.99
• 1/2 chicken all white $10.99
• All come with choice of 2 small sides
• 1 whole chicken family meal ( served with 3 Large sides + 2 liter soda) $23.99
• 2 whole chicken family meal (served with 4 Large sides + 2 liter soda) $33.99
• Extra whole chicken (Chicken only) $13.99
• Sides available with meals:
• - Cilantro infused white rice
• - Hand Cut Fries
• - Hand Cut Sweet potato Fries
• - Yucca
• - Fried Plantains
• - Pinto Beans
• - Black Beans
• - Steamed vegetable medley
• - Cesar Salad
• - Garden Salad
• - House Salad
• - Tortillas
• (reg side: $1.99) Large Side $3.29
• Other Dishes available:
• Lomo Saltado: $12.99
• Pesto Pasta (Tallarin Verde) w/ Steak or 1/4 chicken $ 12.99
• Bistek a lo Pobre: $12.99
• Marcos Treat $12.99 (Chicken filet grilled) w/ salads
• Tallarin Saltado (Garden style pasta) w/ Chicken $11.99, Steak add. $1.49
• Tallarin a la Huancaina $12.99 w/ steak or 1/4 chicken
• Garden Salad ($6.99) Add chicken or steak $1.99
• Cesar Salad ($6.99) Add Chicken or steak $1.99
• House Salad ($6.99) Add chicken or steak $1.99
• DRINKS/DESSERTS:
• - SODAS: REG. $1.99 LARGE 2.59
• - ANDA FIZZ: $1.69 CAN; $1.99 IMPORTED; $2.59 BOTTLE
• - SPECIALTY DRINKS: $2.59
• - ALFAJOR $2.99
• - PERUVIAN FLAN $4.99
• - 3 LECHES $4.99
• (SAVE $1.00 OF ANY DESSERT WITH PURCHASE OF MEAL)
Nice to have
• We would love to see it all in 1 half sheet
Should not have
• can not have too much on it where its confusing.

```html
<!DOCTYPE html>
<html lang="en">
<head>
<meta charset="utf-8">
<title>Los Fogones Ember Poultry Menu</title>
<link rel="stylesheet" href="https://fonts.googleapis.com/css2?family=Lato:wght@400;700&display=swap">
<style>
  :root {
    --page: #ecebe6;
    --wood-dark: #3b1f10;
    --wood-mid: #5a3019;
    --wood-light: #7a4424;
    --wood-edge: #8e5330;
    --ink: #ffffff;
    --ink-soft: #f3e9df;
    --brand: #e9582a;
    --rule: #e8d9cc;
    --food-a: #6f8a3a;
    --food-b: #b0623a;
    --food-c: #d8c9a8;
  }
  * { box-sizing: border-box; margin: 0; padding: 0; }
  html, body { width: 863px; height: 1200px; overflow: hidden; }
  body {
    background: var(--page);
    font-family: "Lato", sans-serif;
    position: relative;
  }

  .panel {
    position: absolute;
    top: 40px;
    height: 923px;
    box-shadow: 0 2px 6px rgba(0,0,0,.25);
  }
  .wood {
    background:
      linear-gradient(90deg,
        var(--wood-edge) 0%, var(--wood-light) 8%, var(--wood-mid) 14%,
        var(--wood-dark) 30%, var(--wood-mid) 50%, var(--wood-dark) 70%,
        var(--wood-mid) 86%, var(--wood-light) 92%, var(--wood-edge) 100%);
  }

  /* Cover */
  .cover { left: 53px; width: 362px; }
  .cover-name {
    position: absolute;
    left: 0; right: 0; top: 510px;
    text-align: center;
    color: var(--brand);
    font-weight: 400;
    font-size: 28px;
    line-height: 1.2;
    letter-spacing: .5px;
  }

  /* Inside */
  .inside { left: 433px; width: 363px; overflow: hidden; }
  .food-strip {
    position: absolute; top: 0; bottom: 0; width: 47px;
    background: linear-gradient(180deg, var(--food-b) 0%, var(--food-c) 25%, var(--food-a) 45%, var(--food-b) 65%, var(--food-a) 85%, var(--food-c) 100%);
  }
  .food-strip.left { left: 0; }
  .food-strip.right { right: 0; }
  .menu-body {
    position: absolute; left: 47px; right: 47px; top: 0; bottom: 0;
  }

  .menu-name {
    position: absolute; left: 0; right: 0; top: 104px;
    text-align: center;
    color: var(--brand);
    font-weight: 400;
    font-size: 21px;
    line-height: 1.15;
  }

  .section {
    position: absolute; left: 0; right: 0;
    text-align: center;
    color: var(--ink);
    font-size: 12px;
    line-height: 15.6px;
  }
  .section h2 {
    font-size: 12px;
    font-weight: 700;
    line-height: 15.6px;
  }
  .section .plain-head { font-weight: 400; }
  .note { font-size: 9.5px; color: var(--ink-soft); }
  .gap { height: 15px; }

  .divider {
    position: absolute; left: 50px; right: 50px; height: 7px;
  }
  .divider svg { display: block; width: 100%; height: 7px; }
</style>
</head>
<body>

  <section class="panel cover wood" aria-label="Menu cover">
    <p class="cover-name">Los Fogones<br>Ember Poultry</p>
  </section>

  <section class="panel inside" aria-label="Menu">
    <div class="food-strip left" role="img" aria-label="Photo strip of grilled chicken, salad and pasta"></div>
    <div class="food-strip right" role="img" aria-label="Photo strip of grilled chicken, rice, yucca and salad"></div>

    <div class="menu-body wood">
      <p class="menu-name">Los Fogones Ember Poultry</p>

      <div class="section" style="top:162px">
        <h2>CHICKEN</h2>
        <div style="height:15px"></div>
        <p>1/4 Chicken Dark .............. $6.99</p>
        <p>1/4 Chicken White .............. $7.99</p>
        <p>1/2 Chicken white + dark .............. $9.99</p>
        <p>1/2 chicken all white .............. $10.99</p>
        <p class="note">(All come with choice of 2 small sides)</p>
        <div class="gap"></div>
        <p>1 whole chicken family meal .............. $23.99</p>
        <p class="note">( served with 3 Large sides + 2 liter soda)</p>
        <p>2 whole chicken family meal ............ $33.99</p>
        <p class="note">(served with 4 Large sides + 2 liter soda)</p>
        <p>Extra whole chicken .............. $13.99</p>
        <p class="note">(Chicken only)</p>
      </div>

      <div class="divider" style="top:392px">
        <svg viewBox="0 0 220 7" preserveAspectRatio="none" aria-hidden="true">
          <line x1="4" y1="3.5" x2="216" y2="3.5" stroke="#e8d9cc" stroke-width="1"/>
          <rect x="1" y="1" width="4" height="4" transform="rotate(45 3 3.5)" fill="#e8d9cc"/>
          <rect x="215" y="1" width="4" height="4" transform="rotate(45 217 3.5)" fill="#e8d9cc"/>
        </svg>
      </div>

      <div class="section" style="top:410px">
        <h2 class="plain-head">SIDES AVAILABLE WITH MEALS:</h2>
        <p>Cilantro infused white rice</p>
        <p>Hand Cut Fries • Hand Cut Sweet potato Fries</p>
        <p>Yucca • Fried Plantains</p>
        <p>Pinto Beans • Black Beans</p>
        <p>Steamed vegetable medley</p>
        <p>Cesar Salad • Garden Salad</p>
        <p>House Salad • Tortillas</p>
        <p>(Reg side: $1.99)</p>
        <p>(Large Side $3.29</p>
      </div>

      <div class="divider" style="top:585px">
        <svg viewBox="0 0 220 7" preserveAspectRatio="none" aria-hidden="true">
          <line x1="4" y1="3.5" x2="216" y2="3.5" stroke="#e8d9cc" stroke-width="1"/>
          <rect x="1" y="1" width="4" height="4" transform="rotate(45 3 3.5)" fill="#e8d9cc"/>
          <rect x="215" y="1" width="4" height="4" transform="rotate(45 217 3.5)" fill="#e8d9cc"/>
        </svg>
      </div>

      <div class="section" style="top:596px">
        <h2 class="plain-head">OTHER DISHES AVAILABLE</h2>
        <div style="height:16px"></div>
        <p>Lomo Saltado ..........$12.99</p>
        <p>Pesto Pasta <span class="note">(Tallarin Verde)</span></p>
        <p>w/ Steak or 1/4 chicken .............. $ 12.99</p>
        <p>Bistek a lo Pobre .............. $12.99</p>
        <p>Marcos Treat .............. $12.99</p>
        <p class="note">(Chicken filet grilled) w/ salads</p>
        <p>Tallarin Saltado .............. $11.99</p>
        <p class="note">(Garden style pasta) w/ Chicken</p>
        <p class="note">Steak add. $1.49</p>
        <p>Tallarin a la Huancaina .............. $12.99</p>
        <p class="note">w/ steak or 1/4 chicken</p>
      </div>

      <div class="divider" style="top:805px">
        <svg viewBox="0 0 220 7" preserveAspectRatio="none" aria-hidden="true">
          <line x1="4" y1="3.5" x2="216" y2="3.5" stroke="#e8d9cc" stroke-width="1"/>
          <rect x="1" y="1" width="4" height="4" transform="rotate(45 3 3.5)" fill="#e8d9cc"/>
          <rect x="215" y="1" width="4" height="4" transform="rotate(45 217 3.5)" fill="#e8d9cc"/>
        </svg>
      </div>

      <div class="section" style="top:814px">
        <p>Garden Salad .............. $6.99)</p>
        <p class="note">Add chicken or steak $1.99</p>
        <p>Cesar Salad ...............$6.99)</p>
        <p class="note">Add Chicken or steak $1.99</p>
        <p>House Salad .............. $6.99)</p>
        <p class="note">Add chicken or steak $1.99</p>
      </div>
    </div>
  </section>

</body>
</html>
```